Flyer Design Project

Painting and Maintenance
This is what I have as idea as Job description
Refresh, renew & revive your home. from painting to carpentry. Do you guys have any epic unique slogan?
As what we do Residential - Commercial Interior - ExteriorTrim & Molding installationWainscoting - Wallpaper removalCabinet refinishing Woodwork EnamelingDeck & Fence Cleaning & SealingPressure washConcrete & Paver Washing
I would like to have a note that says-Prompt professional service-Free estimates-Insured -"visit us on PalPorch"
I would like new ideas from you guys as well!
Carpentry

```html
<!DOCTYPE html>
<html lang="en">
<head>
<meta charset="utf-8">
<title>Painting &amp; Maintenance Flyer</title>
<link href="https://fonts.googleapis.com/css2?family=Montserrat:wght@700&family=Raleway:wght@400&display=swap" rel="stylesheet">
<style>
  :root {
    --brick: #9b4b39;
    --brick-dark: #6e3426;
    --wall-light: #e4e4e2;
    --wall-shade: #b9b7b2;
    --panel-tan: #c38f55;
    --accent-red: #c8282a;
    --ink: #2b2623;
  }
  html, body {
    margin: 0;
    padding: 0;
    overflow: hidden;
    background: #ffffff;
  }
  .flyer {
    position: relative;
    width: 1200px;
    height: 789px;
    overflow: hidden;
    font-family: "Raleway", sans-serif;
    color: var(--ink);
  }
  .backdrop-photo {
    position: absolute;
    left: 0; top: 0;
    width: 662px; height: 789px;
    background: linear-gradient(200deg, var(--brick) 0%, var(--brick-dark) 28%, var(--wall-shade) 45%, var(--wall-light) 62%, #f2f2f0 100%);
  }
  .side-strip-photo {
    position: absolute;
    left: 1127px; top: 0;
    width: 73px; height: 789px;
    background: linear-gradient(180deg, var(--brick-dark), var(--brick) 50%, var(--brick-dark));
  }
  .services-panel {
    position: absolute;
    left: 662px; top: 0;
    width: 465px; height: 789px;
    background: var(--panel-tan);
  }
  .section-title {
    font-family: "Montserrat", sans-serif;
    font-weight: 700;
    color: var(--accent-red);
    margin: 0;
    letter-spacing: 0.5px;
    line-height: 1;
  }
  .services-title {
    position: absolute;
    left: 746px; top: 99px;
    font-size: 41px;
  }
  .services-list {
    position: absolute;
    left: 742px; top: 155px;
    margin: 0; padding: 0;
    list-style: none;
    font-size: 21px;
    line-height: 42px;
  }
  .promise-title {
    position: absolute;
    left: 54px; top: 452px;
    font-size: 41px;
  }
  .promise-list {
    position: absolute;
    left: 54px; top: 507px;
    margin: 0; padding: 0;
    list-style: none;
    font-size: 20.5px;
    line-height: 30.6px;
  }
  .bullet::before {
    content: "\2022";
    font-size: 12px;
    vertical-align: 3px;
    margin-right: 6px;
  }
  .promise-note {
    position: absolute;
    left: 54px; top: 599px;
    width: 330px;
    margin: 0;
    font-size: 20.5px;
    line-height: 30.6px;
  }
  .work-photo {
    position: absolute;
    box-shadow: 6px 8px 14px rgba(0,0,0,0.35);
  }
  .work-photo--bright-kitchen {
    left: 398px; top: 150px; width: 308px; height: 174px;
    background: linear-gradient(135deg, #f4f4f2, #d9dadc 55%, #9c9ea2);
  }
  .work-photo--loft-kitchen {
    left: 398px; top: 345px; width: 313px; height: 182px;
    background: linear-gradient(160deg, #a78e7c, #5a3a2c 45%, #1e1a18);
  }
  .work-photo--island-kitchen {
    left: 398px; top: 546px; width: 308px; height: 179px;
    background: linear-gradient(180deg, #f0efec, #d2cdc6 50%, #4a3a30);
  }
</style>
</head>
<body>
<main class="flyer">
  <div class="backdrop-photo" role="img" aria-label="Photo of a red brick wall behind a white plastered staircase"></div>
  <div class="services-panel"></div>
  <div class="side-strip-photo" role="img" aria-label="Photo of a red brick wall"></div>

  <div class="work-photo work-photo--bright-kitchen" role="img" aria-label="Photo of a bright white kitchen with dining table and staircase"></div>
  <div class="work-photo work-photo--loft-kitchen" role="img" aria-label="Photo of a loft kitchen with brick walls and a wooden table"></div>
  <div class="work-photo work-photo--island-kitchen" role="img" aria-label="Photo of a white-cabinet kitchen with a dark wood island"></div>

  <h2 class="section-title services-title">OUR SERVICES</h2>
  <ul class="services-list">
    <li class="bullet">Residential to Commercial</li>
    <li class="bullet">Interior - Exterior</li>
    <li class="bullet">Trim &amp; Molding Installation</li>
    <li class="bullet">Wainscoting</li>
    <li class="bullet">Wallpaper Removal</li>
    <li class="bullet">Cabinet Refinishing</li>
    <li class="bullet">Woodwork</li>
    <li class="bullet">Enameling</li>
    <li class="bullet">Deck &amp; Fence</li>
    <li class="bullet">Cleaning &amp; Sealing</li>
    <li class="bullet">Pressure wash</li>
    <li class="bullet">Concrete &amp; Paver Washing</li>
  </ul>

  <h2 class="section-title promise-title">OUR PROMISE</h2>
  <ul class="promise-list">
    <li class="bullet">Prompt Professional Service</li>
    <li class="bullet">Free estimates</li>
    <li class="bullet">Quality Ensured</li>
  </ul>
  <p class="promise-note">Visit us on PalPorch for more information or view some of our work.</p>
</main>
</body>
</html>
```